・元々の商品パッケージは写真の通りです。
透明な蓋が掛けてあり、帯シールが貼られているものです。
・新パッケージは写真の通り密閉包装されたものです。
写真はテスト中のため単にシールを貼り付けただけのものになっています。
正式に販売に向けて、こちらの上面のデザイン作成を依頼いたします。
・濃厚焼きチーズケーキのイメージカラーはネイビーです。
濃厚ニューヨークチーズのイメージカラーは深めのレッドです。
ベースカラーを同上にして頂きたいと思います。
デザインは同じで色違いにするだけで販売することを考えています。
ご提案の段階では濃厚焼きチーズのネイビーのパッケージだけで結構です。
依頼確定後、同デザインでレッドのパッケージのものを作って頂けると
ありがたいです。
・弊社スイーツカテゴリーについては「Bel torvame(ベル・トルヴァム)」という
名称でブランディングしておりますので、添付のロゴデータを使って頂くか
同名称をデザインのどこかに入れて頂けますでしょうか。
なお、こちらはフランス語で花を意味する「fleur」と「me(弊社名)」
を合わせた造語です。
・側面にはバーコードや食品表示をしますのでデザイン不要です。
また表面についても全く中身を見えないようにしないで、
商品を見せるために一部透明なままとする考えもあります。
※各種写真は添付ファイルにありますのでご確認ください。
少し不鮮明ですが参考までにご利用ください。

■セールスポイント
・チーズ生地にクリームチーズを69%と贅沢に配合しており、
とにかく濃厚でしっとりした口当たりが特徴。
(一般的に出回っているものは40%前後の比率のものが多いです)
・百貨店やスイーツ専門店にも負けないクオリティのものを
お求めやすい価格で提供。
(同水準のもので比較すると大体専門店の半額ぐらいです)

■商品名
商品名は「濃厚焼きチーズケーキ」および「濃厚ニューヨークチーズケーキ」です。価格は小売店様によって異なりますが500円前後で販売されています。

■商品イメージ
とにかくオシャレで、流行りのピクモ女子達がこぞって欲しくなるような、洗練されたデザインにしたいと思っています。

どちらかというとポップ路線よりも高級でお洒落で落ち着いたパッケージを希望しますが、そこまで厳密にイメージを固めているわけではないので、デザイナー様のセンスを最大限に生かして、世の中をアッと驚かせるような、女性達の目を輝かせるような素敵なデザイン案をいただけたらと思います。
・容器サイズは幅55mm、奥行き165mm、高さ35mmとなります。
上記した通り、表面デザインだけで結構なので
横55×縦165のサイズのデザインを考えて頂けますでしょうか。
各デザイナー様ご提案ありがとうございます。
ご提案を受けて気づいたことがあるので追記させて頂きます。

・小売店様で陳列するときの都合上、デザインは縦型でお願いいたします。
・クリームチーズの配合比率69%はクリームチーズ生地に対しての比率なので、
69%を乗せる場合は、そこを明記願います。
スポンジの土台の上にクリームチーズ生地が乗っている使用なので全体からすれば
クリームチーズ比率が69%あるわけではありません。
・商品画像が不鮮明だったので画像追加させて頂きます。
・トルヴァムのロゴデータですが、社内にaiベースのものがなく、包材メーカー様に確認中です。
入手次第追加させて頂きます。

月間10万本近く販売している主力商品のパッケージリニューアルなので
社運をかけて取り組んでいる案件です。

皆様どうぞよろしくお願いいたします。
デザインの参考になるかどうかわかりませんが、
「月間10万本売れている商品なのに何故リニューアルをするのか」について
追記させて頂きます。

一番大きな要因は消費期限の長期化です。
密閉包装し脱酸素剤を一緒に封入することで、現状5日間⇒14日に長期化することが可能となります。

消費期限が長期化することで、お店のほうで大量陳列をしてもロスなく販売できる。
大量陳列することでお客様の目に止まりやすくなる販売数量が増える。

ということを見込んでいます。

よろしくお願いします。
既存のトルヴァムロゴのイラストレーター形式のデータについて添付させて頂きます。
上記した通り、こちらは無理に使用頂かなくても結構です。

よろしくお願いいたします。
追記いたします。

各デザイナー様、ご提案ありがとうございます。
色々とデザインを頂き考えたのですが、やはり添付のトルヴァムロゴをデザインに使用して頂くようお願いいたします。

理由としては、
①現在のパッケージでも売れており、一定のお客様がついてくれている人気商品なので
同じロゴを使用することで、同一商品のリニューアルだということ明確にしたいため。
②今回リニューアル対象とないの弊社スイーツ、カフェゼリー、杏仁豆腐等々にもトルヴァムロゴが
使われているため、リニューアル後も弊社スイーツブランドとして統一感を持たせたいため。

申し訳ありませんが、よろしくお願いいたします。

・シンプルながら高級感があるところ。
・フォントがレトロでお洒落なところ。
・ブルー、レッドを基調とする中でゴールドのアクセントが入った色使い。
等々、全体的なデザインが気に入りました。

たくさんのご提案を頂きありがとうございました。

販促ポスターや包装パッケージ等、今後もワークピアを活用させて頂きますので、
また機会がございましたら、よろしくお願いいたします。

```html
<!DOCTYPE html>
<html lang="ja">
<head>
<meta charset="utf-8">
<title>Bel torvame 濃厚ニューヨークチーズケーキ</title>
<link href="https://fonts.googleapis.com/css2?family=Bodoni+Moda:wght@800&family=Shippori+Mincho:wght@600&family=Zen+Maru+Gothic:wght@500&display=swap" rel="stylesheet">
<style>
  :root {
    --ink-dark: #2b211f;
    --cream: #f6f1e6;
    --ribbon-red: #c0202c;
    --text-light: #fbf6ee;
    --text-dark: #3a302c;
    --plate: #eceae6;
    --cake: #ecd98e;
  }
  html, body {
    margin: 0;
    padding: 0;
    width: 1200px;
    height: 3520px;
    overflow: hidden;
    background: var(--ink-dark);
  }
  .package-top {
    position: relative;
    width: 1200px;
    height: 3520px;
    overflow: hidden;
    background: var(--ink-dark);
  }
  .backdrop {
    position: absolute;
    inset: 0;
  }
  .brand-name {
    position: absolute;
    left: 420px;
    top: 40px;
    width: 360px;
    text-align: center;
    font-family: "Bodoni Moda", serif;
    font-weight: 800;
    font-size: 64px;
    line-height: 1;
    color: var(--text-light);
    letter-spacing: 1px;
  }
  .product-title-en {
    position: absolute;
    left: 880px;
    top: 1230px;
    transform: translate(-50%, -50%) rotate(90deg);
    white-space: nowrap;
    font-family: "Bodoni Moda", serif;
    font-weight: 800;
    font-size: 196px;
    line-height: 1;
    letter-spacing: 6px;
    color: var(--text-light);
  }
  .product-title-ja {
    position: absolute;
    left: 672px;
    top: 440px;
    writing-mode: vertical-rl;
    font-family: "Shippori Mincho", serif;
    font-weight: 600;
    font-size: 72px;
    letter-spacing: 12px;
    line-height: 1;
    color: var(--text-light);
  }
  .serving-art {
    position: absolute;
    left: 0;
    top: 2380px;
  }
</style>
</head>
<body>
<main class="package-top">
  <svg class="backdrop" width="1200" height="3520" viewBox="0 0 1200 3520" aria-hidden="true">
    <path class="cream-panel" fill="var(--cream)"
      d="M0,960 C0,420 420,140 1200,120 L1200,1760 C1200,2860 1160,3280 1080,3520 L0,3520 Z"/>
    <path class="ribbon" fill="var(--ribbon-red)"
      d="M648,230 L984,230 L984,2200 L816,2100 L648,2200 Z"/>
  </svg>

  <div class="brand-name">Bel torvame</div>

  <div class="product-title-ja">濃厚ニューヨークチーズケーキ</div>
  <div class="product-title-en">CHEESE CAKE</div>

  <svg class="serving-art" width="1200" height="700" viewBox="0 0 1200 700">
    <defs>
      <path id="tagline-arc" d="M300,240 Q640,60 960,220"/>
      <linearGradient id="plate-tone" x1="0" y1="0" x2="1" y2="1">
        <stop offset="0" stop-color="#f4f2ee"/>
        <stop offset="0.55" stop-color="var(--cake)"/>
        <stop offset="1" stop-color="#d9d6d1"/>
      </linearGradient>
    </defs>
    <text font-family="'Zen Maru Gothic', sans-serif" font-weight="500" font-size="46" fill="var(--text-dark)" letter-spacing="3">
      <textPath href="#tagline-arc" startOffset="50%" text-anchor="middle">濃厚でしっとりした口当たり</textPath>
    </text>
    <ellipse role="img" aria-label="白いお皿にのったチーズケーキとフォークのイラスト"
      cx="620" cy="480" rx="440" ry="200" fill="url(#plate-tone)"/>
  </svg>
</main>
</body>
</html>
```